Redesign of the labels for our cosmetic brand Su Dulcaria

We need to redesign all the labels for our pharmaceutical cosmetic brand. It must be inspired in the old time apothecary and compounding pharmacies. Our aim is to emulate old pharmacy bottles and jars, as our cosmetics are formulated as they used to be prepared; with the highest amount of actives and always based in Nature
We have attached our actual catalogue so you can get an idea of who we are. Also we have attached some of our old style labels. We changed them last year but they havent been atractive enough

Target Market(s)

Pharmaceutical cosmetics

Industry/Entity Type

Pharmaceutical

Requirements
Must have
• The labels must have a vintage touch, like old pharmacy jars

```html
<!DOCTYPE html>
<html lang="en">
<head>
<meta charset="utf-8">
<title>Su Dulcaria – Dropper Label</title>
<link rel="stylesheet" href="https://fonts.googleapis.com/css2?family=Libre+Caslon+Text:wght@400;700&display=swap">
<style>
  :root {
    --page: #ffffff;
    --paper-light: #f8eed6;
    --paper-dark: #ecdcb6;
    --frame-navy: #3a4668;
    --frame-orange: #d9874a;
    --ornament: #e7b98a;
    --ornament-soft: #f0d3ae;
    --brand-ink: #5e5246;
    --title-red: #b83a2a;
    --body-ink: #3c322a;
  }
  html, body {
    margin: 0;
    padding: 0;
    width: 828px;
    height: 1200px;
    overflow: hidden;
    background: var(--page);
  }
  .label-canvas {
    display: block;
    width: 828px;
    height: 1200px;
  }
  .brand-arc {
    font-family: "Libre Caslon Text", serif;
    font-size: 40px;
    letter-spacing: 3px;
    fill: var(--brand-ink);
  }
  .product-name {
    font-family: "Libre Caslon Text", serif;
    font-weight: 700;
    font-size: 44px;
    letter-spacing: 1px;
    fill: var(--title-red);
  }
  .product-description {
    font-family: "Libre Caslon Text", serif;
    font-size: 30px;
    fill: var(--body-ink);
  }
  .volume {
    font-family: "Libre Caslon Text", serif;
    font-size: 28px;
    fill: var(--body-ink);
  }
  .frame-navy { fill: none; stroke: var(--frame-navy); }
  .frame-orange { fill: none; stroke: var(--frame-orange); }
  .rule-navy { stroke: var(--frame-navy); stroke-width: 3; }
  .rule-orange { stroke: var(--frame-orange); stroke-width: 2; }
  .ornament { fill: var(--ornament); }
  .ornament-soft { fill: var(--ornament-soft); }
</style>
</head>
<body>
<svg class="label-canvas" viewBox="0 0 828 1200" xmlns="http://www.w3.org/2000/svg">
  <defs>
    <linearGradient id="paper" x1="0" y1="0" x2="0" y2="1">
      <stop offset="0" stop-color="var(--paper-light)"/>
      <stop offset="1" stop-color="var(--paper-dark)"/>
    </linearGradient>
    <path id="brand-curve" d="M 224 340 A 420 420 0 0 1 604 340"/>
  </defs>

  <!-- label paper -->
  <rect class="label-paper" x="104" y="110" width="620" height="980" fill="url(#paper)"/>

  <!-- frames -->
  <rect class="frame-navy" x="118" y="124" width="592" height="952" stroke-width="5"/>
  <rect class="frame-orange" x="132" y="138" width="564" height="924" stroke-width="2"/>
  <rect class="frame-navy" x="140" y="146" width="548" height="908" stroke-width="1.5"/>

  <!-- corner ornaments -->
  <g role="img" aria-label="Floral corner flourishes in soft orange">
    <rect class="ornament-soft" x="152" y="158" width="70" height="80" rx="26"/>
    <rect class="ornament-soft" x="606" y="158" width="70" height="80" rx="26"/>
    <rect class="ornament-soft" x="152" y="962" width="70" height="80" rx="26"/>
    <rect class="ornament-soft" x="606" y="962" width="70" height="80" rx="26"/>
  </g>
  <g role="img" aria-label="Floral side vines in soft orange">
    <rect class="ornament-soft" x="152" y="380" width="26" height="480" rx="13"/>
    <rect class="ornament-soft" x="650" y="380" width="26" height="480" rx="13"/>
  </g>

  <!-- brand arc -->
  <text class="brand-arc" text-anchor="middle">
    <textPath href="#brand-curve" startOffset="50%">SU DULCARIA</textPath>
  </text>

  <!-- ornament under brand -->
  <rect class="ornament" x="274" y="400" width="280" height="40" rx="20" role="img" aria-label="Scrolled floral divider"/>

  <!-- product name band -->
  <line class="rule-navy" x1="200" y1="520" x2="628" y2="520"/>
  <line class="rule-orange" x1="200" y1="530" x2="628" y2="530"/>
  <text class="product-name" x="414" y="588" text-anchor="middle">PRODUCT NAME</text>
  <line class="rule-orange" x1="200" y1="618" x2="628" y2="618"/>
  <line class="rule-navy" x1="200" y1="628" x2="628" y2="628"/>

  <!-- description -->
  <text class="product-description" x="414" y="720" text-anchor="middle">Product description</text>

  <!-- ornament under description -->
  <rect class="ornament" x="294" y="770" width="240" height="36" rx="18" role="img" aria-label="Small scrolled floral divider"/>

  <!-- volume -->
  <text class="volume" x="414" y="900" text-anchor="middle">30 ml</text>

  <!-- bottom ornament -->
  <rect class="ornament" x="314" y="950" width="200" height="36" rx="18" role="img" aria-label="Bottom floral flourish"/>
</svg>
</body>
</html>
```